Web Design Project - Investor Services

I would like a simple and elegant web design for my company "Torvelo Management". The company will provide services to Corporate and Institutional investors for their needs with local/foreign investment vehicles. The website will have four pages to start: home, about us, services, contact.
I already chose a logo, and I will attach the source file. The color that I will most probably use for the logo will be blue, and i also like grey with a white background. For the website I would like to see light colors, maybe light green or grey, with the logo either in blue, grey or white (depeding on the background).
Target Market(s)
Investment managers and tax/legal advisors from top firms. This is the reason why I want something simple and elegant.
Industry/Entity Type
Investment
Requirements
Nice to have
- I do not want many pictures in the website, but I might include a couple of pictures of Madrid and maybe a picture of myself in the about us page (still deciding). I will attach some pictures of Madrid that I like, but feel free to search for others - i have others but i am not able to attach all of them.

```html
<!DOCTYPE html>
<html lang="en">
<head>
<meta charset="utf-8">
<title>Torvelo Management</title>
<link href="https://fonts.googleapis.com/css2?family=Alegreya:ital,wght@0,500;1,500&family=Fira+Sans+Condensed:ital,wght@0,300;0,400;0,500;1,300&display=swap" rel="stylesheet">
<style>
:root{
  --blue:#1e2a8c;
  --nav:#333a44;
  --green:#67a82c;
  --green-dark:#4f8a1c;
  --band:#f1f1f1;
  --text:#4a4a4a;
  --line:#dcdcdc;
  --card-in:#f3f3f3;
  --photo-top:#6f8794;
  --photo-mid:#8b98a2;
  --photo-low:#3b4650;
}
*{margin:0;padding:0;box-sizing:border-box}
html,body{width:1200px;height:1054px;overflow:hidden;background:#fff}
body{position:relative;font-family:"Fira Sans Condensed",Arial,sans-serif;color:var(--text)}
.site-header{position:absolute;left:0;top:0;width:1200px;height:67px;background:#fff;box-shadow:0 2px 4px rgba(0,0,0,.12);z-index:3}
.brand{position:absolute;left:146px;top:8px;font-weight:300;color:var(--blue);font-size:40px;letter-spacing:.5px;line-height:48px}
.brand-divider{position:absolute;left:363px;top:0;width:1px;height:67px;background:#c8c8c8}
.brand-sub{position:absolute;left:386px;top:14px;font-weight:300;color:var(--blue);font-size:30px;line-height:36px}
.main-nav{position:absolute;top:24px;left:687px;display:flex}
.main-nav a{font-size:15px;font-weight:500;color:var(--nav);text-decoration:none;margin-right:18px}
.main-nav a.current{color:var(--blue)}
.login{position:absolute;left:968px;top:0;width:90px;height:67px;background:var(--green);color:#fff;font-weight:500;font-size:15px;display:flex;align-items:center;justify-content:center;gap:10px}
.login span{width:18px;height:18px;border-radius:50%;background:#2f5c14;font-size:11px;display:flex;align-items:center;justify-content:center}
.hero-band{position:absolute;left:0;top:67px;width:1200px;height:517px;background:var(--band)}
.slider{position:absolute;left:135px;top:0;width:927px;height:515px;background:#fff;box-shadow:0 0 3px rgba(0,0,0,.25)}
.slider-photo{position:absolute;left:4px;top:0;width:919px;height:465px;background:linear-gradient(180deg,var(--photo-top) 0%,var(--photo-mid) 45%,#5d6a74 75%,var(--photo-low) 100%)}
.slider-bar{position:absolute;left:4px;top:465px;width:919px;height:46px;background:linear-gradient(180deg,#5c6770,#6a737a)}
.pager{position:absolute;left:419px;top:476px;width:86px;height:25px;border-radius:13px;background:#fff;display:flex;align-items:center;justify-content:center;gap:6px}
.pager i{width:11px;height:11px;border-radius:50%;border:1px solid #b9b9b9;background:#f4f4f4}
.pager i.on{background:#cfcfcf}
.welcome{position:absolute;left:0;top:606px;width:1194px;text-align:center}
.welcome h1{font-family:"Alegreya",serif;font-style:italic;font-weight:500;font-size:24px;line-height:32px;color:#3d3d3d}
.welcome h1 em{color:var(--green)}
.welcome p{margin-top:6px;font-style:italic;font-weight:300;font-size:15.5px;line-height:23px;color:#444}
.card{position:absolute;top:719px;width:277px;height:184px;border:1px solid #d2d2d2;background:#fff;padding:3px}
.card-inner{position:relative;width:100%;height:100%;background:var(--card-in);padding:16px 17px}
.card h2{display:flex;align-items:center;gap:12px;font-family:"Alegreya",serif;font-weight:500;font-size:22px;line-height:28px;color:#333}
.card p{margin-top:6px;font-weight:300;font-size:15px;line-height:23px;color:#333;white-space:nowrap}
.more{position:absolute;left:17px;top:132px;width:56px;height:29px;background:var(--green);border-bottom:2px solid var(--green-dark);color:#fff;font-weight:500;font-size:15.5px;text-align:center;line-height:28px}
.card.contact .more{top:134px}
.site-footer{position:absolute;left:136px;top:934px;width:909px;border-top:1px solid var(--line);text-align:center}
.footer-nav{margin-top:18px;font-size:14px;color:#444}
.footer-nav a{color:#444;text-decoration:none;margin:0 8px}
.footer-nav a.current{color:var(--green-dark)}
.copy{font-size:13.5px;color:#444;margin-top:4px}
.social{display:flex;justify-content:center;gap:6px;margin-top:14px}
.social i{width:22px;height:22px;border-radius:3px;background:#3f6aa8}
.social i+i{background:#4b8fd0}
</style>
</head>
<body>
<header class="site-header">
  <div class="brand">torvelo</div>
  <div class="brand-divider"></div>
  <div class="brand-sub">management</div>
  <nav class="main-nav">
    <a class="current" href="#">Home</a>
    <a href="#">About Us</a>
    <a href="#">Services</a>
    <a href="#">Contact Us</a>
  </nav>
  <div class="login">Login <span>v</span></div>
</header>

<div class="hero-band">
  <div class="slider">
    <div class="slider-photo" role="img" aria-label="Madrid skyline with four tall office towers under a pale blue sky"></div>
    <div class="slider-bar"></div>
    <div class="pager"><i class="on"></i><i></i><i></i><i></i></div>
  </div>
</div>

<section class="welcome">
  <h1>Welcome to <em>Torvelo Management</em></h1>
  <p>The company will provide services to Corporate and Institutional investors for their<br>needs with local/foreign investment vehicles.</p>
</section>

<article class="card" style="left:139px">
  <div class="card-inner">
    <h2><svg width="20" height="26" viewBox="0 0 20 26"><path d="M3 0h14v7l-4 3H7L3 7z" fill="#333"/><circle cx="10" cy="17" r="8" fill="#333"/><path d="M10 12l1.5 3.2 3.4.4-2.5 2.3.7 3.4-3.1-1.7-3.1 1.7.7-3.4-2.5-2.3 3.4-.4z" fill="#f3f3f3"/></svg>About Us</h2>
    <p>The company will provide services<br>tInvestment managers and tax/legal<br>advisors from top firms.</p>
    <span class="more">More</span>
  </div>
</article>

<article class="card" style="left:453px">
  <div class="card-inner">
    <h2><svg width="26" height="24" viewBox="0 0 26 24"><path d="M8 4V1h10v3" fill="none" stroke="#333" stroke-width="2"/><rect x="0" y="5" width="26" height="19" rx="2" fill="#333"/><rect x="5" y="5" width="2" height="19" fill="#f3f3f3"/><rect x="19" y="5" width="2" height="19" fill="#f3f3f3"/></svg>Services</h2>
    <p>The company will provide services<br>tInvestment managers and tax/legal<br>advisors from top firms.</p>
    <span class="more">More</span>
  </div>
</article>

<article class="card contact" style="left:768px">
  <div class="card-inner">
    <h2><svg width="28" height="26" viewBox="0 0 28 26"><path d="M0 11L14 0l14 11v15H0z" fill="#333"/><rect x="5" y="5" width="18" height="12" fill="#f3f3f3"/><path d="M0 11l14 10 14-10v15H0z" fill="#333"/><path d="M1 25l10-7M27 25l-10-7" stroke="#f3f3f3" stroke-width="1.5"/></svg>Contact Us</h2>
    <p style="letter-spacing:-.2px">Write here something about your<br>company address and phone no, email<br>id etc for your esteemed clients.</p>
    <span class="more">More</span>
  </div>
</article>

<footer class="site-footer">
  <nav class="footer-nav"><a class="current" href="#">Home</a> | <a href="#">About Us</a> | <a href="#">Services</a> | <a href="#">Contact Us</a></nav>
  <p class="copy">Copyright@2013, Torvelo Management</p>
  <div class="social"><i></i><i></i></div>
</footer>
</body>
</html>
```